Harwick Legal

To update and modernize current business card appearance. Marta's business is based in Melbourne with 4 other lawyers in the firm. Marta travels to the Pilbara in Western Australia approximately 1 week a month as part of the firms legal work. She consults with clients in Newman, Tom Price and Port Hedland. The lawyers work mostly from a home office, apart from court appearances. They have a virtual office in Melbourne city, and use facilities in 3 or 4 other locations around Melbourne. It is important the client's think this is a conventional law firm with a permanent office. Our business structure is a difficult concept for them to grasp. The business has been operational for 3 years, growing from 1 lawyer to 4 lawyers during that time. Our website is www.Harwicklegal.example.au and is currently being upgraded as we are not happy with its content. The logo is currently orange and dark grey but the orange is a difficult colour to reproduce and often turns out "poo" brown when documents are printed. We need clients to know we are user friendly and caring - and not head up our rears ends as some lawyers appear to be.
Updates

Thank you for the feedback so far. 1. Some of the designs have too much black (We prefer darker grey & not too much.) 2. Happy for designers to play around with different colours & logo design. What we're after is a modern look and business card that people say "wow" when they pick it up.

Industry/Entity Type

Business

```html
<!DOCTYPE html>
<html lang="en">
<head>
<meta charset="utf-8">
<title>Harwick Legal – Business Card</title>
<link href="https://fonts.googleapis.com/css2?family=Libre+Baskerville:wght@400;700&display=swap" rel="stylesheet">
<style>
  :root {
    --navy: #1b4a86;
    --navy-deep: #123c74;
    --grey-text: #6b6b6b;
    --grey-line: #8a8a8a;
    --card: #fbfbfb;
    --page: #e4e6e8;
  }
  * { box-sizing: border-box; margin: 0; padding: 0; }
  html, body { width: 1200px; height: 919px; overflow: hidden; }
  body {
    background: var(--page);
    font-family: "Libre Baskerville", "Times New Roman", serif;
    position: relative;
  }
  .card {
    position: absolute;
    width: 720px;
    height: 410px;
    background: var(--card);
    border-radius: 26px;
    box-shadow: 0 6px 18px rgba(0,0,0,.18);
    overflow: hidden;
  }
  .card--front { left: 60px; top: 40px; }
  .card--back { left: 420px; top: 469px; }

  /* Front */
  .brand {
    position: absolute; right: 46px; top: 58px;
    display: flex; align-items: center; gap: 10px;
  }
  .brand__mark { width: 14px; height: 14px; background: var(--navy); }
  .brand__name {
    color: var(--navy); font-size: 24px; letter-spacing: 2px;
    text-transform: uppercase; font-weight: 400;
  }
  .brand-rule {
    position: absolute; right: 40px; top: 102px; width: 200px;
    border-top: 1px solid var(--grey-line);
  }
  .holder { position: absolute; left: 40px; top: 196px; right: 40px; }
  .holder__line { display: flex; align-items: baseline; gap: 16px; }
  .holder__name {
    color: var(--navy); font-weight: 700; font-size: 25px; letter-spacing: .5px;
  }
  .holder__creds { color: var(--grey-text); font-size: 13px; }
  .holder__rule { border-top: 1px solid var(--grey-line); margin: 6px 0 6px; }
  .holder__area { color: var(--grey-text); font-size: 13px; }

  .contact {
    position: absolute; left: 40px; bottom: 34px;
    display: grid; grid-template-columns: auto auto; column-gap: 12px; row-gap: 3px;
    font-size: 13.5px;
  }
  .contact dt { color: var(--navy); font-weight: 700; }
  .contact dd { color: var(--grey-text); }
  .address {
    position: absolute; right: 40px; bottom: 100px;
    text-align: right; color: var(--grey-text); font-size: 13px; line-height: 1.45;
  }

  /* Back */
  .practice__title {
    position: absolute; left: 0; right: 0; top: 88px; text-align: center;
    color: var(--navy); font-weight: 700; font-size: 22px; letter-spacing: 1.5px;
  }
  .practice__band {
    position: absolute; left: 0; right: 0; top: 136px; height: 84px;
    background: linear-gradient(90deg, rgba(27,74,134,0) 0%, var(--navy) 16%, var(--navy-deep) 50%, var(--navy) 84%, rgba(27,74,134,0) 100%);
    color: #fff; text-align: center; font-size: 15px; line-height: 1.6;
    display: flex; flex-direction: column; justify-content: center;
  }
  .tagline {
    position: absolute; left: 0; right: 0; top: 256px; text-align: center;
    color: #2a2a2a; font-size: 24px; letter-spacing: 1px;
    display: flex; justify-content: center; align-items: center; gap: 22px;
  }
  .tagline__sep { width: 10px; height: 10px; background: #222; }
  .inquiries {
    position: absolute; left: 0; right: 0; bottom: 0; height: 66px;
    background: var(--navy);
    color: #fff; font-size: 19px; font-weight: 700; letter-spacing: .5px;
    display: flex; align-items: center; justify-content: center;
  }
</style>
</head>
<body>

<section class="card card--front" aria-label="Business card front">
  <div class="brand">
    <span class="brand__mark"></span>
    <span class="brand__name">Harwick Legal</span>
  </div>
  <div class="brand-rule"></div>

  <div class="holder">
    <div class="holder__line">
      <span class="holder__name">J. MARTA ASHDOWN</span>
      <span class="holder__creds">LLB (Hons) - Accredited Mediator</span>
    </div>
    <div class="holder__rule"></div>
    <div class="holder__area">Melbourne Eastern And Bayside Suburbs</div>
  </div>

  <dl class="contact">
    <dt>Phone</dt><dd>(130)-055-0142 (1300 Harwick)</dd>
    <dt>Mobile</dt><dd>(041)-555-0187</dd>
    <dt>Email</dt><dd>marta.ashdown@harwicklegal.example.au</dd>
    <dt>Web</dt><dd>www.Harwicklegal.example.au</dd>
  </dl>

  <address class="address" style="font-style:normal">
    RM 1208 Kestrel Tower 145<br>Harbour Rd Wanchai H.K.
  </address>
</section>

<section class="card card--back" aria-label="Business card back">
  <h2 class="practice__title">- AREAS OF PRACTICE -</h2>
  <div class="practice__band">
    <span>Family Law • Intervention Orders • Collaborative Practice</span>
    <span>Criminal Law • Mediation &amp; Negotiation</span>
  </div>
  <p class="tagline">
    <span>Experience</span><span class="tagline__sep"></span>
    <span>Support</span><span class="tagline__sep"></span>
    <span>Solutions</span>
  </p>
  <div class="inquiries">Inquiries : info@harwicklegal.example.au</div>
</section>

</body>
</html>
```